Business Card Design

We need a business card for our established Fruit and Veg shop that offers retail and wholesale to the public. We offer a range of Australian products and also provide nuts, confectionary, pasta's etc. We would like to use colours green, red, orange and yellow. The final design would use our photo of the shop and some produce and should communicate freshness and quality.

Target Market(s)

families, businesses

Industry/Entity Type

Retail

Contact Information for Business Card

Wattlebrook Produce Shed
Retail and Wholesale Fruit and Veg
Peter and Marco Bellucci - Manager
47 Kestrel Ridge Drive, Dunmore Vale S.A. 5163
Ph: (08) 8294 3516
Fax: (08) 8294 3617
wattlebrookproduceshed@mailvane.net
www.socialpage.net/WattlebrookProduceShed
Open 7 Days

Requirements
Must have
• The photo of the shop
Nice to have
• Both the photos

```html
<!DOCTYPE html>
<html lang="en">
<head>
<meta charset="utf-8">
<title>Wattlebrook Produce Shed – Business Card</title>
<link href="https://fonts.googleapis.com/css2?family=Lobster&family=Gochi+Hand&display=swap" rel="stylesheet">
<style>
  :root {
    --stage: #d9d9db;
    --card-light: #f1f1ee;
    --yellow: #f7d21a;
    --orange: #f0a018;
    --title-orange: #e8771a;
    --red: #d5122a;
    --green: #1e9a3c;
    --white: #ffffff;
    --sky-top: #eef1f4;
    --sky-low: #c9d2da;
    --shed-roof: #aab2b8;
    --shed-dark: #3c3f44;
    --produce-red: #d8434b;
    --produce-yellow: #e3cd46;
    --produce-green: #8cae3f;
  }
  * { box-sizing: border-box; margin: 0; padding: 0; }
  html, body { width: 1200px; height: 750px; overflow: hidden; }
  body {
    background: var(--stage);
    display: flex;
    align-items: center;
    justify-content: center;
    gap: 60px;
  }
  .card {
    position: relative;
    width: 520px;
    height: 300px;
    border-radius: 24px;
    overflow: hidden;
    box-shadow: 0 4px 14px rgba(0,0,0,0.18);
  }

  /* Front */
  .card-front { background: var(--card-light); }
  .front-heading {
    position: absolute;
    top: 26px; left: 0; right: 0;
    text-align: center;
    font-family: "Lobster", cursive;
    font-weight: 400;
    color: var(--title-orange);
    line-height: 1.15;
  }
  .front-heading .shop-name { font-size: 21px; display: block; white-space: nowrap; }
  .front-heading .shop-line { font-size: 32px; display: block; }
  .shop-photo {
    position: absolute;
    left: 0; right: 0; bottom: 0;
    height: 180px;
    background: linear-gradient(180deg, var(--sky-top) 0%, var(--sky-low) 35%, var(--shed-roof) 55%, var(--shed-dark) 100%);
  }

  /* Back */
  .card-back { background: linear-gradient(160deg, var(--yellow) 0%, var(--yellow) 45%, var(--orange) 100%); }
  .back-art { position: absolute; inset: 0; }
  .back-info {
    position: absolute;
    top: 22px; left: 212px; right: 12px;
    font-family: "Gochi Hand", cursive;
    color: var(--red);
  }
  .back-title {
    font-family: "Lobster", cursive;
    color: var(--title-orange);
    font-size: 13px;
    line-height: 1.2;
    white-space: nowrap;
  }
  .back-tagline {
    display: flex;
    align-items: baseline;
    gap: 10px;
    font-family: "Lobster", cursive;
    color: var(--green);
    font-size: 22px;
    line-height: 1.2;
    margin-left: 30px;
  }
  .role {
    font-family: "Gochi Hand", cursive;
    font-size: 12px;
    color: var(--green);
  }
  .manager-name { font-size: 19px; line-height: 1.2; margin: 2px 0 4px; }
  .contact-list { list-style: none; font-size: 13px; line-height: 1.35; }
  .contact-list li { display: flex; align-items: flex-start; gap: 6px; }
  .contact-list .icon { flex: none; width: 14px; height: 14px; margin-top: 2px; }
  .contact-list .web, .contact-list .mail { font-size: 12px; white-space: nowrap; }
  .open-days {
    margin-top: 6px;
    color: var(--green);
    font-size: 24px;
    letter-spacing: 0.5px;
    padding-left: 20px;
  }
</style>
</head>
<body>

  <section class="card card-front">
    <h1 class="front-heading">
      <span class="shop-name">Wattlebrook Produce Shed Retail and Wholesale</span>
      <span class="shop-line">Fruit and Veg</span>
    </h1>
    <div class="shop-photo" role="img" aria-label="Photo of the produce shed storefront under a pale sky"></div>
  </section>

  <section class="card card-back">
    <svg class="back-art" width="520" height="300" viewBox="0 0 520 300">
      <defs>
        <linearGradient id="produceTones" x1="0" y1="0" x2="1" y2="1">
          <stop offset="0" stop-color="#7a5a3c"/>
          <stop offset="0.35" stop-color="#d8434b"/>
          <stop offset="0.6" stop-color="#8cae3f"/>
          <stop offset="1" stop-color="#e3cd46"/>
        </linearGradient>
      </defs>
      <path class="red-band" d="M0,0 H176 C130,90 150,210 262,300 H0 Z" fill="var(--red)"/>
      <path d="M0,0 H160 C114,90 134,210 244,300 H0 Z" fill="url(#produceTones)" role="img" aria-label="Photo of fresh fruit and vegetable displays with apples and bananas"/>
    </svg>

    <div class="back-info">
      <p class="back-title">Wattlebrook Produce Shed Retail and Wholesale</p>
      <p class="back-tagline">Fruit and Veg <span class="role">manager</span></p>
      <p class="manager-name">Peter and Marco Bellucci</p>
      <ul class="contact-list">
        <li>
          <svg class="icon" viewBox="0 0 14 14"><circle cx="7" cy="7" r="7" fill="var(--green)"/><path d="M7 3a2.4 2.4 0 0 0-2.4 2.4C4.6 7.3 7 10.8 7 10.8s2.4-3.5 2.4-5.4A2.4 2.4 0 0 0 7 3z" fill="var(--white)"/></svg>
          <span>47 Kestrel Ridge Drive,<br>Dunmore Vale S.A. 5163</span>
        </li>
        <li>
          <svg class="icon" viewBox="0 0 14 14"><circle cx="7" cy="7" r="7" fill="var(--green)"/><path d="M4.5 3.5l1.6-.3.8 2-1 .8c.5 1 1.2 1.7 2.1 2.1l.8-1 2 .8-.3 1.6c-3.3.2-6.2-2.7-6-6z" fill="var(--white)"/></svg>
          <span>(08) 8294 3516 &nbsp;Fax (08) 8294 3617</span>
        </li>
        <li>
          <svg class="icon" viewBox="0 0 14 14"><circle cx="7" cy="7" r="7" fill="var(--green)"/><rect x="3.5" y="4.5" width="7" height="5" fill="var(--white)"/><path d="M3.5 4.5L7 7.3l3.5-2.8" fill="none" stroke="var(--green)" stroke-width="0.8"/></svg>
          <span class="mail">wattlebrookproduceshed@mailvane.net</span>
        </li>
        <li>
          <svg class="icon" viewBox="0 0 14 14"><circle cx="7" cy="7" r="7" fill="var(--green)"/></svg>
          <span class="web">www.socialpage.net/WattlebrookProduceShed</span>
        </li>
      </ul>
      <p class="open-days">Open 7 Days</p>
    </div>
  </section>

</body>
</html>
```